Web design for our new company

We need a web design for our product and for our company.
And the main is our Product tool called "velmora".
----------------------------------------------------------
[Our company's Goal]
Make organization’s communication smooth and healthy with transparency and efficiency for works and tasks in all levels with our workflow tool.

[Our Mission]
Our mission is to achieve business goals with customers.
We work together to identify the goals for your company, guides your strategy and bring the technology answers which best fit to achieve the goals.

[What we do]
We have a workflow tool "velmora"
- Very simple end-user configurable workflow for any company processes
(Targeting small-med size company)
- Graphical & fun features for startup users
- Simple and easy task control with quillbox e-mail look & feel
- Non charged skill up guidance
- Additional features with;
Multiple delegation
Clear status for each owner
Task owner management console with due date reminders&reporting

Others
1. System Development & Implementation Service
Our client list includes a wide variety of small to medium to major sized enterprises.
We can offer from full-scratch based development to packaged system implementation.

2. Project Management(PM) Service
We will provide end-to-end PM service with experienced PM.
Our service is not only “managing” but “leading” to bring success to achieve the goal.

3.Consultation Service

Consulting services to a wide range of fields such as creating business strategy, business process Kaizen, IT system consultation and change management.

Target Market(s)

Business to Business
Mainly to medium size - startup company

Industry/Entity Type

It Company

Coding

Coded - Design and coding required

Number of Pages Required

5+ page

Colors
0255a3
33a6d7
86cfc6
33b8a4
add136
cadf82
fbf289
fee18a
faa54b

Requirements
Must have
• We need Pages for
• Company mission
• Service Overview
• Contact
• Privacy Policy
• Terms and Conditions
• =========================
• As there were some questions, I add followings.---------
• 1. File Format
• We are going to use Brixel cloud services to upload finished web files.
• The finished files should be ready to use by simply replacing images and text.
• Please provide me "easy to handle" template with "sophisticated design".
• Thanks!
• 2. Multiple Languages
• We need buttons for changing language.
• We will have this translated to German, English and Japanese.
• Thank you so much!!
Nice to have
• These are current Logos and will be a next project to revise them...
• Attached Company Profile and Logo design
• 1. Company Profile
• 2. Our Company Logo
• 3. Our Product Logo -> This is most close to our image of design base.
• 4. Product Logo for PPT Header
• All just for your reference.
• ---------
• As there were some request, I added attachment as for contents for Our mission page.
Should not have
• I hope to see some unique designs.
• (Sorry please ignore my last update as I checked with our CEO.
• Bootstrap is absolutely good template.)

```html
<!DOCTYPE html>
<html lang="en">
<head>
<meta charset="utf-8">
<title>Korvani – Home</title>
<link rel="stylesheet" href="https://fonts.googleapis.com/css2?family=Comfortaa:wght@700&family=Montserrat:ital,wght@0,400;0,500;0,600;0,700;0,800;1,400;1,600&display=swap">
<style>
:root{
  --header-yellow:#f7e36a;
  --button-yellow:#fcd93a;
  --hero-top:#def5e6;
  --hero-bottom:#f3e5a6;
  --olive:#b8ad6a;
  --icon-yellow:#f2d33a;
  --ink:#151515;
  --ink-soft:#3a3a3a;
  --brand-blue:#0255a3;
  --brand-green:#7f9a28;
  --footer-grey:#efefef;
  --white:#ffffff;
}
*{box-sizing:border-box;margin:0;padding:0}
html,body{width:1200px;height:1200px;overflow:hidden;background:var(--white)}
body{position:relative;font-family:"Montserrat",sans-serif;color:var(--ink)}
.page{position:absolute;left:319px;top:0;width:563px;height:1188px}
.abs{position:absolute}

/* header */
.site-header{left:0;top:0;width:563px;height:54px;background:var(--header-yellow)}
.brand-tab{left:57px;top:0;width:36px;height:54px;background:var(--white);display:flex;align-items:center;justify-content:center}
.brand-tab span{font-size:7px;font-weight:700;color:var(--brand-green)}
.lang-switch{left:112px;top:20px;display:flex;gap:3px;font-size:7px;font-weight:600}
.lang-switch a{display:block;padding:2px 4px;color:var(--ink);text-decoration:none;border:1px solid rgba(0,0,0,.25)}
.lang-switch a.is-current{background:var(--ink);color:var(--header-yellow);border-color:var(--ink)}
.main-nav{left:0;top:0;width:563px;height:54px;font-size:7.5px}
.main-nav a{position:absolute;top:22px;color:var(--ink);text-decoration:none;transform:translateX(-50%);white-space:nowrap}

/* hero */
.hero{left:0;top:54px;width:563px;height:263px;background:linear-gradient(180deg,var(--hero-top) 0%,#eaf0cf 45%,var(--hero-bottom) 100%);text-align:center}
.hero h1{position:absolute;left:0;right:0;top:78px;font-family:"Comfortaa",sans-serif;font-weight:700;font-size:29px;color:var(--ink)}
.hero p{position:absolute;left:0;right:0;top:121px;font-style:italic;font-size:9.3px;line-height:12.8px;color:var(--ink-soft)}
.btn{position:absolute;display:flex;align-items:center;justify-content:center;font-weight:600;text-decoration:none}
.hero .btn{left:227px;top:184px;width:108px;height:31px;background:var(--button-yellow);color:var(--ink);font-size:9px}

/* process cards */
.process{left:19px;top:316px;width:524px;height:154px;display:flex;box-shadow:0 18px 22px rgba(0,0,0,.07)}
.process-card{flex:1;background:var(--white);position:relative;text-align:center}
.process-card.is-active{background:var(--olive);color:var(--white)}
.process-card svg{position:absolute;left:50%;top:30px;transform:translateX(-50%)}
.process-card h3{position:absolute;left:0;right:0;top:110px;font-size:18px;font-weight:800}

/* services */
.section-title{left:0;top:518px;width:563px;text-align:center;font-family:"Comfortaa",sans-serif;font-weight:700;font-size:27px;-webkit-text-stroke:.6px var(--ink)}
.product-line{left:0;top:557px;width:563px;text-align:center;font-size:8.5px;color:var(--ink-soft)}
.product-line b{color:var(--brand-green);font-weight:700}
.service{top:594px;width:150px;text-align:center;transform:translateX(-50%)}
.service svg{display:block;margin:0 auto}
.service p{margin-top:18px;font-size:8.3px;font-weight:600;line-height:10.3px}

/* banner */
.banner{left:0;top:704px;width:563px;height:220px;background:linear-gradient(160deg,#3b3d3e 0%,#232425 45%,#111 100%);text-align:center}
.banner p{position:absolute;left:0;right:0;top:55px;color:var(--white);font-style:italic;font-weight:600;font-size:11.6px;line-height:23px}
.banner .btn{left:220px;top:126px;width:122px;height:31px;background:var(--brand-blue);color:var(--white);font-size:8.6px}

/* footer */
.footer-brand{left:0;top:972px;width:563px;text-align:center;font-weight:700;font-size:20px;color:var(--brand-green)}
.contact-band{left:0;top:1031px;width:563px;height:131px;background:var(--footer-grey)}
.contact-item{top:26px;width:150px;text-align:center;transform:translateX(-50%)}
.contact-item svg{display:block;margin:0 auto}
.contact-item p{margin-top:20px;font-size:8.4px;font-weight:600;line-height:10px}
.copyright{left:0;top:1174px;width:563px;text-align:center;font-size:8px;font-weight:600}
</style>
</head>
<body>
<div class="page">

  <header class="abs site-header">
    <div class="abs brand-tab"><span>Korvani</span></div>
    <div class="abs lang-switch" aria-label="Language">
      <a href="#" class="is-current">EN</a><a href="#">DE</a><a href="#">JA</a>
    </div>
    <nav class="abs main-nav">
      <a href="#" style="left:228px">Home</a>
      <a href="#" style="left:276px">About us</a>
      <a href="#" style="left:327px">Pricing</a>
      <a href="#" style="left:375px">Product</a>
      <a href="#" style="left:440px">OverviewPolicy</a>
      <a href="#" style="left:511px">Contact Us</a>
    </nav>
  </header>

  <section class="abs hero">
    <h1>WELCOME TO KORVANI</h1>
    <p>Our mission is to achieve business goals with customers.<br>
    We work together to identify the goals for your company, guides your strategy and<br>
    bring the technology answers which best fit to achieve the goals.</p>
    <a class="btn" href="#">Contact Us</a>
  </section>

  <section class="abs process">
    <div class="process-card">
      <svg width="56" height="56" viewBox="0 0 56 56" fill="none" stroke="var(--icon-yellow)" stroke-width="2">
        <rect x="20" y="2" width="16" height="11"/><path d="M28 13v10M8 23h40M8 23v16M28 23v16M48 23v16"/>
        <rect x="2" y="39" width="12" height="14"/><rect x="22" y="41" width="12" height="14"/><rect x="42" y="39" width="12" height="14"/>
      </svg>
      <h3>Plan</h3>
    </div>
    <div class="process-card is-active">
      <svg width="64" height="62" viewBox="0 0 64 62" fill="none" stroke="var(--white)" stroke-width="2">
        <path d="M14 34a10 10 0 0 1 2-20a16 16 0 0 1 31 2a9 9 0 0 1 3 18z"/>
        <path d="M20 34v14M28 34v20M36 34v20M44 34v14"/>
        <circle cx="20" cy="51" r="3"/><circle cx="28" cy="57" r="3"/><circle cx="36" cy="57" r="3"/><circle cx="44" cy="51" r="3"/>
      </svg>
      <h3>Develop</h3>
    </div>
    <div class="process-card">
      <svg width="62" height="62" viewBox="0 0 62 62" fill="none" stroke="var(--icon-yellow)" stroke-width="2">
        <path d="M58 4c-16 0-28 10-36 26l10 10C48 32 58 20 58 4z"/><circle cx="43" cy="19" r="5"/>
        <path d="M22 30l-12-2-6 8 14 2M32 40l2 12 8-6-2-14M20 42l-10 12M16 36l-8 6"/>
      </svg>
      <h3>Launch</h3>
    </div>
  </section>

  <h2 class="abs section-title">What we do</h2>
  <p class="abs product-line">Our workflow tool <b>velmora</b> keeps every task clear, simple and on time.</p>

  <div class="abs service" style="left:110px">
    <svg width="48" height="36" viewBox="0 0 48 36" fill="none" stroke="var(--ink)" stroke-width="2.4">
      <rect x="2" y="2" width="34" height="24"/><path d="M19 26v6M11 33h16"/>
      <circle cx="19" cy="14" r="4"/><path d="M30 34l14-14M34 22l10 10"/>
    </svg>
    <p>System Development &amp;<br>Implementation Service</p>
  </div>
  <div class="abs service" style="left:281px">
    <svg width="52" height="36" viewBox="0 0 52 36" fill="var(--ink)">
      <path d="M12 2h38v26H26v-3h21V5H15v8h-3z"/><rect x="22" y="8" width="10" height="12"/><rect x="36" y="10" width="8" height="7"/>
      <circle cx="10" cy="19" r="4"/><path d="M2 34c0-8 3-11 8-11h10l4-4 2 2-5 7H16v6z"/>
    </svg>
    <p>Project Management(PM)<br>Service</p>
  </div>
  <div class="abs service" style="left:456px">
    <svg width="46" height="36" viewBox="0 0 46 36">
      <circle cx="24" cy="12" r="7.5" fill="none" stroke="var(--ink)" stroke-width="4"/>
      <circle cx="24" cy="12" r="10" fill="none" stroke="var(--ink)" stroke-width="3.5" stroke-dasharray="3.5 4.35"/>
      <path d="M3 20h7l6 4h10a2.5 2.5 0 0 1 0 5H18v1h9l10-6a3 3 0 0 1 4 4L29 35H12l-9-5z" fill="var(--ink)"/>
    </svg>
    <p>Consultation Service</p>
  </div>

  <section class="abs banner" role="img" aria-label="Dark photo of business people working at a laptop on a wooden desk">
    <p>We do our best to provide professional results to you. We believe that<br>this isn't achievable through providing a small part of the service.</p>
    <a class="btn" href="#">Contact Us Now</a>
  </section>

  <div class="abs footer-brand">Korvani</div>

  <section class="abs contact-band">
    <div class="abs contact-item" style="left:99px">
      <svg width="28" height="38" viewBox="0 0 28 38"><path d="M14 1a13 13 0 0 0-13 13c0 10 13 23 13 23s13-13 13-23A13 13 0 0 0 14 1z" fill="#3a3a3a"/><circle cx="14" cy="14" r="5" fill="var(--footer-grey)"/></svg>
      <p>B – 4120 Halden Mühlen<br>str. 7</p>
    </div>
    <div class="abs contact-item" style="left:281px">
      <svg width="36" height="38" viewBox="0 0 36 38"><path d="M6 3l7-2 5 10-4 4c2 5 5 9 10 12l4-4 9 6-2 7c-3 2-8 2-13-1C13 30 6 21 3 13 1 8 3 5 6 3z" fill="#3a3a3a"/><path d="M22 2a14 14 0 0 1 12 12M21 8a8 8 0 0 1 7 7" fill="none" stroke="#3a3a3a" stroke-width="2.4"/></svg>
      <p>0 5550-182-347</p>
    </div>
    <div class="abs contact-item" style="left:460px">
      <svg width="46" height="38" viewBox="0 0 46 38" fill="none" stroke="#3a3a3a" stroke-width="2.4"><rect x="2" y="4" width="42" height="30"/><path d="M2 4l21 18L44 4M2 34l16-14M44 34L28 20"/></svg>
      <p>info@korvani.com</p>
    </div>
  </section>

  <p class="abs copyright">Copyright © 2018 Korvani</p>
</div>
</body>
</html>
```